Vintage "Greetings from Door County" Design for Wall

I are looking to recreate the vintage "Greetings from" postcard graphic from the 1940-50s. The main focus will be the saying "Greetings from Door County". Door County is a resort area in Wisconsin and we will use this graphic as a backdrop for tourist's instagram pictures. The letters of "Door County" will include things that the area is known for such as swimming, fishing, beaches, boating, biking, camping, cherry orchards, sunsets on the water etc. I have attached an actual postcard from the 50s for Door County to help you visualize the project (Picture 1). I have also attached landmarks and iconic features of Door County to include in the letters (Pictures 2-10). I want it to be more whimsical in nature with drawings to depict these landmarks as opposed to actual realistic pictures (Example 1 & 2). Please ask any questions to help clarify the project. Thanks and good luck!
Target Market(s)
Tourists
Industry/Entity Type
Retail
Colors
Designer to choose colors to be used in the design.
Look and feel
Each slider illustrates characteristics of the customer's brand and the style your logo design should communicate.

```html
<!DOCTYPE html>
<html lang="en">
<head>
<meta charset="utf-8">
<title>Greetings from Door County, Wisconsin</title>
<link rel="stylesheet" href="https://fonts.googleapis.com/css2?family=Titan+One&family=Yellowtail&display=swap">
<style>
  :root {
    --page: #ffffff;
    --card-edge: #b9b7a6;
    --card-face: #d6d4c2;
    --sky-top: #c4582a;
    --sky-mid: #d4743c;
    --water: #b3612f;
    --water-deep: #9a5a2c;
    --shore: #3b3a22;
    --ink: #0d0d0d;
    --outline: #ffffff;
  }
  html, body {
    margin: 0;
    padding: 0;
    width: 1200px;
    height: 840px;
    overflow: hidden;
    background: var(--page);
  }
  .postcard {
    display: block;
    width: 1200px;
    height: 840px;
  }
  .script-line {
    font-family: "Yellowtail", cursive;
    fill: var(--ink);
    stroke: var(--outline);
    stroke-width: 5;
    paint-order: stroke;
  }
  .block-letter {
    font-family: "Titan One", sans-serif;
    text-anchor: middle;
  }
  .block-letter .letter-shadow {
    fill: var(--ink);
    stroke: var(--ink);
    stroke-width: 12;
    stroke-linejoin: round;
  }
  .block-letter .letter-face {
    stroke: var(--outline);
    stroke-width: 7;
    stroke-linejoin: round;
    paint-order: stroke;
  }
  .block-letter .letter-rim {
    fill: none;
    stroke: var(--ink);
    stroke-width: 1.5;
  }
</style>
</head>
<body>
<svg class="postcard" viewBox="0 0 1200 840" xmlns="http://www.w3.org/2000/svg" aria-labelledby="card-title">
  <title id="card-title">Greetings from Door County, Wisconsin</title>
  <defs>
    <linearGradient id="scene-sunset" x1="0" y1="0" x2="0" y2="1">
      <stop offset="0" stop-color="var(--sky-top)"/>
      <stop offset="0.45" stop-color="var(--sky-mid)"/>
      <stop offset="0.47" stop-color="var(--water)"/>
      <stop offset="0.75" stop-color="var(--water-deep)"/>
      <stop offset="0.86" stop-color="var(--shore)"/>
      <stop offset="1" stop-color="var(--shore)"/>
    </linearGradient>
    <linearGradient id="fill-d" x1="0" y1="0" x2="0" y2="1"><stop offset="0" stop-color="#3f5a9a"/><stop offset="0.5" stop-color="#c9683a"/><stop offset="1" stop-color="#4d86a8"/></linearGradient>
    <linearGradient id="fill-o1" x1="0" y1="0" x2="0" y2="1"><stop offset="0" stop-color="#3f7a2e"/><stop offset="0.4" stop-color="#4a6a48"/><stop offset="1" stop-color="#2f8fa0"/></linearGradient>
    <linearGradient id="fill-o2" x1="0" y1="0" x2="0" y2="1"><stop offset="0" stop-color="#6fb2e0"/><stop offset="0.45" stop-color="#e03a2a"/><stop offset="1" stop-color="#3d86c4"/></linearGradient>
    <linearGradient id="fill-r" x1="0" y1="0" x2="0" y2="1"><stop offset="0" stop-color="#5c9a3a"/><stop offset="0.55" stop-color="#7aa845"/><stop offset="1" stop-color="#3c6a3c"/></linearGradient>
    <linearGradient id="fill-c" x1="0" y1="0" x2="0" y2="1"><stop offset="0" stop-color="#6aa8dc"/><stop offset="0.6" stop-color="#4a5f70"/><stop offset="1" stop-color="#c08a3a"/></linearGradient>
    <linearGradient id="fill-o3" x1="0" y1="0" x2="0" y2="1"><stop offset="0" stop-color="#3ab7b5"/><stop offset="0.5" stop-color="#c4283a"/><stop offset="1" stop-color="#46a7b0"/></linearGradient>
    <linearGradient id="fill-u" x1="0" y1="0" x2="0" y2="1"><stop offset="0" stop-color="#4f9ad6"/><stop offset="0.5" stop-color="#2f78a8"/><stop offset="1" stop-color="#b2602e"/></linearGradient>
    <linearGradient id="fill-n" x1="0" y1="0" x2="0" y2="1"><stop offset="0" stop-color="#e0781e"/><stop offset="0.45" stop-color="#f2b428"/><stop offset="1" stop-color="#5a6a3a"/></linearGradient>
    <linearGradient id="fill-t" x1="0" y1="0" x2="0" y2="1"><stop offset="0" stop-color="#5aa6e4"/><stop offset="0.5" stop-color="#c84a3a"/><stop offset="1" stop-color="#2f6ea0"/></linearGradient>
    <linearGradient id="fill-y" x1="0" y1="0" x2="0" y2="1"><stop offset="0" stop-color="#8cc0e6"/><stop offset="0.5" stop-color="#7a5a40"/><stop offset="1" stop-color="#3a86b8"/></linearGradient>
  </defs>

  <!-- card stock -->
  <rect class="card-edge" x="16" y="44" width="1170" height="756" rx="18" fill="var(--card-edge)"/>
  <rect class="card-face" x="22" y="50" width="1158" height="744" rx="14" fill="var(--card-face)"/>

  <!-- sunset scene behind the lettering -->
  <rect class="backdrop-scene" role="img" aria-label="Sunset over the lake with a dark wooded shoreline"
        x="40" y="62" width="1120" height="714" rx="10" fill="url(#scene-sunset)"/>

  <!-- Greetings from -->
  <text class="script-line greeting" font-size="150" transform="translate(150 300) rotate(-22)">Greetings</text>
  <text class="script-line greeting-from" font-size="120" transform="translate(170 500) rotate(-42)">from</text>

  <!-- DOOR -->
  <g class="block-word word-door" font-size="380">
    <g class="block-letter" role="img" aria-label="Letter D showing a lakeside barn and rocky shore" transform="translate(416 456) rotate(-6) scale(0.62 1)">
      <text class="letter-shadow" x="12" y="14">D</text>
      <text class="letter-face" fill="url(#fill-d)">D</text>
      <text class="letter-rim">D</text>
    </g>
    <g class="block-letter" role="img" aria-label="Letter O showing a wooded cliff above blue water" transform="translate(590 446) rotate(-8) scale(0.62 1)">
      <text class="letter-shadow" x="12" y="14">O</text>
      <text class="letter-face" fill="url(#fill-o1)">O</text>
      <text class="letter-rim">O</text>
    </g>
    <g class="block-letter" role="img" aria-label="Letter O showing a red tour boat at the harbour" transform="translate(790 414) rotate(-9) scale(0.66 1)">
      <text class="letter-shadow" x="12" y="14">O</text>
      <text class="letter-face" fill="url(#fill-o2)">O</text>
      <text class="letter-rim">O</text>
    </g>
    <g class="block-letter" role="img" aria-label="Letter R showing goats grazing on a grassy roof" transform="translate(988 384) rotate(-10) scale(0.62 1)">
      <text class="letter-shadow" x="12" y="14">R</text>
      <text class="letter-face" fill="url(#fill-r)">R</text>
      <text class="letter-rim">R</text>
    </g>
  </g>

  <!-- COUNTY -->
  <g class="block-word word-county" font-size="300">
    <g class="block-letter" role="img" aria-label="Letter C showing a wooden lookout tower" transform="translate(168 718) rotate(-4) scale(0.62 1)">
      <text class="letter-shadow" x="12" y="14">C</text>
      <text class="letter-face" fill="url(#fill-c)">C</text>
      <text class="letter-rim">C</text>
    </g>
    <g class="block-letter" role="img" aria-label="Letter O showing ripe cherries on a branch" transform="translate(330 726) rotate(-5) scale(0.62 1)">
      <text class="letter-shadow" x="12" y="14">O</text>
      <text class="letter-face" fill="url(#fill-o3)">O</text>
      <text class="letter-rim">O</text>
    </g>
    <g class="block-letter" role="img" aria-label="Letter U showing a lighthouse on a rocky breakwater" transform="translate(506 702) rotate(-6) scale(0.62 1)">
      <text class="letter-shadow" x="12" y="14">U</text>
      <text class="letter-face" fill="url(#fill-u)">U</text>
      <text class="letter-rim">U</text>
    </g>
    <g class="block-letter" role="img" aria-label="Letter N showing a fish boil fire" transform="translate(684 678) rotate(-6) scale(0.62 1)">
      <text class="letter-shadow" x="12" y="14">N</text>
      <text class="letter-face" fill="url(#fill-n)">N</text>
      <text class="letter-rim">N</text>
    </g>
    <g class="block-letter" role="img" aria-label="Letter T showing a signpost of distances above a marina" transform="translate(844 622) rotate(-5) scale(0.62 1)">
      <text class="letter-shadow" x="12" y="14">T</text>
      <text class="letter-face" fill="url(#fill-t)">T</text>
      <text class="letter-rim">T</text>
    </g>
    <g class="block-letter" role="img" aria-label="Letter Y showing a harbour with a wooden pier" transform="translate(992 638) rotate(-4) scale(0.62 1)">
      <text class="letter-shadow" x="12" y="14">Y</text>
      <text class="letter-face" fill="url(#fill-y)">Y</text>
      <text class="letter-rim">Y</text>
    </g>
  </g>

  <!-- state -->
  <text class="script-line state-name" font-size="84" transform="translate(764 748) rotate(-4)">Wisconsin</text>
</svg>
</body>
</html>
```